Finch Haulage Ltd

We need an A5 size (UK size) flyer to advertise our new business which is called Finch Haulage.
Domestic and Commercial Waste Clearance Services.
Please have the question in bold "Do you have a pile of junk you need to dispose of?"
We collect all kinds of junk or rubbish from homes and businesses across Kent, Sussex and South London.
No fuss, no mess!
A low cost, hassle free alternative to skip hire.
Licensed by the Landcare Board and fully insured (this can be in small print at the bottom).
Please put the Recycle symbol somewhere.
Our tagline on our vehicle is "We Clear More, For Less!"
We'd like the flyer to be bold and eye-catching (to catch the eye of the homeowner or business owner while it's sitting on their doormat).
We need our telephone, website and email to be prominent. Maybe saying "Call today for a free quote"
Tel. 01734 586019
Email: info@finchhaulage.example.co.uk
www.finchhaulage.example.co.uk
Target Market(s)
Our market will be homes and small businesses around Kent, Sussex and South London.

```html
<!DOCTYPE html>
<html lang="en">
<head>
<meta charset="utf-8">
<title>Finch Haulage – Waste Clearance Flyer</title>
<link href="https://fonts.googleapis.com/css2?family=Anton&family=Montserrat:wght@400;700;800&family=Oswald:wght@500;700&display=swap" rel="stylesheet">
<style>
  :root {
    --backdrop: #ece6dc;
    --yellow: #efe836;
    --red: #e3302a;
    --blue: #2f73c3;
    --ink: #1d1d1b;
    --logo-grey: #4a4b4d;
    --logo-green: #2e9a53;
    --white: #ffffff;
  }
  * { margin: 0; padding: 0; box-sizing: border-box; }
  html, body {
    width: 992px; height: 1200px; overflow: hidden;
    background: var(--backdrop);
  }
  .flyer {
    position: absolute; left: 126px; top: 77px;
    width: 740px; height: 1046px;
    background: var(--yellow);
    overflow: hidden;
    box-shadow: 0 4px 18px rgba(0,0,0,.15);
    font-family: "Montserrat", sans-serif;
  }
  .brand-bar {
    position: absolute; left: 0; top: 0; width: 100%; height: 130px;
    display: flex; align-items: center; justify-content: space-between;
    padding: 0 44px;
  }
  .brand {
    display: flex; align-items: center; gap: 14px;
    font-weight: 800; font-size: 40px; color: var(--logo-grey); letter-spacing: 1px;
  }
  .brand-dot { width: 26px; height: 26px; border-radius: 50%; background: var(--logo-green); }
  .tagline {
    font-weight: 800; font-size: 30px; line-height: 1.1; color: var(--red);
  }
  .photo {
    position: absolute; left: 0; top: 130px; width: 100%; height: 340px;
    background: linear-gradient(160deg, #b9bec6 0%, #8d8f94 35%, #a88a55 65%, #6f8f3e 100%);
  }
  .question-intro {
    position: absolute; left: 40px; top: 412px;
    font-weight: 800; font-size: 40px; line-height: 1.1; color: var(--white);
  }
  .headline { font-weight: normal; }
  .headline span { position: absolute; left: 36px; white-space: nowrap; line-height: 1; }
  .headline .junk {
    top: 478px; font-family: "Anton", sans-serif; font-size: 96px; color: var(--red);
  }
  .headline .need {
    top: 588px; left: 40px; font-family: "Montserrat", sans-serif; font-weight: 800;
    font-size: 48px; color: var(--blue);
  }
  .headline .dispose {
    top: 644px; font-family: "Anton", sans-serif; font-size: 118px; color: var(--blue);
  }
  .recycle { position: absolute; right: 44px; top: 500px; width: 64px; height: 64px; }
  .info-row {
    position: absolute; left: 36px; right: 40px; top: 790px;
    display: flex; align-items: center; justify-content: space-between; gap: 20px;
  }
  .promise {
    background: var(--red); border-radius: 14px; padding: 10px 18px;
    font-family: "Oswald", sans-serif; font-weight: 700; line-height: 1.2;
    white-space: nowrap;
  }
  .promise .headline-promise { display: block; color: var(--white); font-size: 26px; }
  .promise .prices { display: block; color: var(--ink); font-size: 19px; }
  .service-note {
    width: 300px; font-size: 22px; line-height: 1.25; color: var(--ink); text-align: center;
  }
  .contact-line {
    position: absolute; left: 0; width: 100%; top: 898px; text-align: center;
    font-family: "Oswald", sans-serif; font-weight: 700; line-height: 1.2;
    font-size: 24px; color: var(--ink); white-space: nowrap;
  }
  .contact-line .divider { color: var(--red); margin: 0 6px; }
  .web-band {
    position: absolute; left: 0; top: 944px; width: 100%; height: 66px;
    background: var(--red); display: flex; align-items: center; justify-content: center;
    font-family: "Anton", sans-serif; font-size: 44px; line-height: 1;
    color: var(--white); letter-spacing: .5px; white-space: nowrap;
  }
  .licence {
    position: absolute; left: 0; top: 1018px; width: 100%; text-align: center;
    font-size: 13px; line-height: 1.2; color: var(--ink);
  }
</style>
</head>
<body>
  <article class="flyer">
    <header class="brand-bar">
      <div class="brand"><span class="brand-dot"></span>Finch Haulage</div>
      <p class="tagline">We Clear More,<br>For Less!</p>
    </header>

    <div class="photo" role="img" aria-label="Photo of a customer with a calculator beside a pile of discarded furniture and boxes"></div>
    <p class="question-intro">Do you have a</p>

    <h1 class="headline">
      <span class="junk">pile of junk</span>
      <span class="need">you need to</span>
      <span class="dispose">dispose of?</span>
    </h1>

    <svg class="recycle" viewBox="0 0 64 64" aria-label="Recycle symbol" role="img">
      <g fill="none" stroke="#e3302a" stroke-width="7" stroke-linecap="round">
        <path d="M24 14 L32 6 L42 20"/>
        <path d="M52 34 L56 46 L40 50"/>
        <path d="M22 52 L8 48 L14 32"/>
      </g>
      <g fill="#e3302a">
        <polygon points="40,12 50,24 36,26"/>
        <polygon points="46,56 34,50 44,42"/>
        <polygon points="6,28 20,28 14,40"/>
      </g>
    </svg>

    <div class="info-row">
      <div class="promise">
        <span class="headline-promise">No fuss, no mess!</span>
        <span class="prices">Very competitive prices.</span>
      </div>
      <p class="service-note">We collect all kinds of junk or rubbish from homes and business.</p>
    </div>

    <p class="contact-line">Tel. 01734 586019<span class="divider">|</span>Email: info@finchhaulage.example.co.uk</p>

    <div class="web-band">www.finchhaulage.example.co.uk</div>
    <p class="licence">Licensed by the Landcare Board and fully insured</p>
  </article>
</body>
</html>
```